Professional
Mark Elwood
President
4217 Vista Arroyo Place, NW
Albuquerque, NM 87114
melwood@emibq.com
www.emibq.com
New Construction*Remodels* Renovations*Handyman Services
Here is my logo for the stationary and business cards
Logo .AI file

```html
<!DOCTYPE html>
<html lang="en">
<head>
<meta charset="utf-8">
<title>Elwood Masonry, Inc — Business Card</title>
<link href="https://fonts.googleapis.com/css2?family=PT+Sans:wght@400;700&display=swap" rel="stylesheet">
<style>
  :root {
    --brand-red: #e3262b;
    --brand-orange: #f6a81c;
    --ink: #2b2b2b;
    --paper: #ffffff;
    --backdrop: #ececec;
  }
  * { margin: 0; padding: 0; box-sizing: border-box; }
  html, body {
    width: 1200px;
    height: 778px;
    overflow: hidden;
    background: var(--backdrop);
    font-family: "PT Sans", Arial, sans-serif;
  }
  .business-card {
    position: absolute;
    left: 40px;
    top: 24px;
    width: 1120px;
    height: 730px;
    border-radius: 40px;
    overflow: hidden;
    background: var(--paper);
    box-shadow: 0 4px 14px rgba(0,0,0,0.18);
  }
  .card-header-art {
    position: absolute;
    inset: 0;
    width: 100%;
    height: 100%;
  }
  .header-red { fill: var(--brand-red); }
  .header-swoosh { fill: var(--brand-orange); }
  .person {
    position: absolute;
    right: 30px;
    top: 178px;
    text-align: right;
    color: var(--paper);
    font-weight: 700;
  }
  .person-name { font-size: 40px; line-height: 1.1; }
  .person-title { font-size: 29px; line-height: 1.2; }
  .company {
    position: absolute;
    left: 34px;
    top: 198px;
    display: flex;
    align-items: center;
    gap: 22px;
  }
  .company-dot {
    width: 124px;
    height: 124px;
    border-radius: 50%;
    background: var(--brand-orange);
  }
  .company-name {
    font-size: 50px;
    font-weight: 700;
    color: var(--ink);
    line-height: 1;
  }
  .address {
    position: absolute;
    left: 44px;
    top: 406px;
    font-size: 31px;
    color: var(--ink);
  }
  .contact-list {
    position: absolute;
    left: 50px;
    top: 450px;
    list-style: none;
  }
  .contact-item {
    display: flex;
    align-items: center;
    height: 40.5px;
    font-size: 30px;
    color: var(--ink);
  }
  .contact-icon {
    width: 24px;
    height: 24px;
    margin-right: 18px;
    fill: var(--brand-orange);
    flex: none;
  }
</style>
</head>
<body>
  <div class="business-card">
    <svg class="card-header-art" viewBox="0 0 1120 730" aria-hidden="true">
      <path class="header-red" d="M0,0 H1120 V500 C700,95 250,70 0,150 Z"/>
      <path class="header-swoosh" d="M0,150 C250,70 700,95 1120,500 V522 C700,125 250,92 0,185 Z"/>
    </svg>

    <div class="person">
      <div class="person-name">Mark Elwood</div>
      <div class="person-title">President</div>
    </div>

    <div class="company">
      <div class="company-dot"></div>
      <div class="company-name">ELWOOD MASONRY, INC</div>
    </div>

    <p class="address">4217 Vista Arroyo Place, NW, Albuquerque, NM 87114</p>

    <ul class="contact-list">
      <li class="contact-item">
        <svg class="contact-icon" viewBox="0 0 24 24" aria-hidden="true">
          <path d="M6.6 10.8a15.1 15.1 0 0 0 6.6 6.6l2.2-2.2a1 1 0 0 1 1-.25 11.4 11.4 0 0 0 3.6.57 1 1 0 0 1 1 1V20a1 1 0 0 1-1 1A17 17 0 0 1 3 4a1 1 0 0 1 1-1h3.5a1 1 0 0 1 1 1c0 1.25.2 2.45.57 3.6a1 1 0 0 1-.25 1z"/>
        </svg>
        505-318-4620
      </li>
      <li class="contact-item">
        <svg class="contact-icon" viewBox="0 0 24 24" aria-hidden="true">
          <path d="M7 1h10a2 2 0 0 1 2 2v18a2 2 0 0 1-2 2H7a2 2 0 0 1-2-2V3a2 2 0 0 1 2-2zm0 4v13h10V5zm5 14.5a1.2 1.2 0 1 0 0 2.4 1.2 1.2 0 0 0 0-2.4z"/>
        </svg>
        505-276-9153
      </li>
      <li class="contact-item">
        <svg class="contact-icon" viewBox="0 0 24 24" aria-hidden="true">
          <path d="M2 5h20v14H2zm2 2v.5l8 5 8-5V7zm0 2.9V17h16V9.9l-8 5z"/>
        </svg>
        melwood@emibq.com
      </li>
      <li class="contact-item">
        <svg class="contact-icon" viewBox="0 0 24 24" aria-hidden="true">
          <path d="M12 2a10 10 0 1 0 0 20 10 10 0 0 0 0-20zm-1 17.9A8 8 0 0 1 4.1 11H7l2 2v2l2 2zm6.9-2.5A2 2 0 0 0 16 16h-1v-3a1 1 0 0 0-1-1H8v-2h2a1 1 0 0 0 1-1V7h2a2 2 0 0 0 2-2v-.4a8 8 0 0 1 2.9 12.8z"/>
        </svg>
        www.emibq.com
      </li>
    </ul>
  </div>
</body>
</html>
```